Brill Insurance Agency - Business Cards

Hello, I am needing new trendy business cards for our Insurance Agency now that I have a new Logo. I have attached our new logo with several color options along with a business card design that I like. I am leaning towards burgundy and blue colors. I have attached our current business card. I have also attached a headshot of our company president, Martin Vale, that you can use if you wish. Thank you so much in advance for all the wonderful designs!!!!

Target Market(s)

We want to look very professional to potential customers and we also want to look very professional so insurance companies will want to contract with us to sell their product.

Industry/Entity Type

Insurance

Contact Information for Business Card

Martin Vale
mvale@brillagency.com
Business: 555-213-4087
Fax: 555-213-7751
Cell: 555-390-2618
Toll Free: 888-555-0194
42 W Elm Rd Butler, MO 64730
www.brillagency.net

Font styles to use
Serif
Sans Serif

Colors
0355a3
3277b5
f04a50
ec1f27

Requirements
Nice to have
• I love creativity. The more creative and balanced a business card design the more I will like it. I would like the card to be printed horizontally instead of vertically.
Should not have
• My project should not have the Allied Coverage Network logo. It is no longer used in the industry.

```html
<!DOCTYPE html>
<html lang="en">
<head>
<meta charset="utf-8">
<title>Brill Insurance Agency – Business Cards</title>
<link rel="stylesheet" href="https://fonts.googleapis.com/css2?family=Montserrat:wght@600&family=Roboto:wght@400;500&display=swap">
<style>
  :root {
    --page-bg: #e9e7e3;
    --card-white: #ffffff;
    --teal: #14a38b;
    --navy-dark: #1d2457;
    --navy-light: #2c3b86;
    --ink: #4a4a4a;
    --ink-soft: #555555;
    --rule: #9a9a9a;
    --ghost: #ebebeb;
  }
  * { margin: 0; padding: 0; box-sizing: border-box; }
  html, body { width: 900px; height: 1200px; overflow: hidden; }
  body {
    position: relative;
    background: var(--page-bg);
    font-family: "Roboto", Arial, sans-serif;
  }
  .card {
    position: absolute;
    left: 82px;
    width: 733px;
    height: 427px;
    border-radius: 22px;
    overflow: hidden;
    box-shadow: 0 4px 10px rgba(0,0,0,0.25);
  }
  .card-front { top: 138px; background: var(--card-white); }
  .card-back {
    top: 633px;
    background: radial-gradient(ellipse at 85% 5%, var(--navy-light) 0%, var(--navy-dark) 60%);
  }

  .ghost-ring { position: absolute; left: 412px; top: -18px; }

  .brand { position: absolute; display: flex; align-items: center; }
  .brand-dot { width: 14px; height: 14px; border-radius: 50%; margin-right: 14px; }
  .brand-name {
    font-family: "Montserrat", Arial, sans-serif;
    font-weight: 600;
    line-height: 1.08;
    text-transform: uppercase;
  }
  .brand-name span { display: block; }
  .brand-name .sub { letter-spacing: 0.24em; font-size: 0.68em; text-align: center; }

  .card-front .brand { left: 44px; top: 74px; }
  .card-front .brand-dot { background: var(--teal); }
  .card-front .brand-name { color: var(--teal); font-size: 28px; }

  .card-back .brand { left: 0; right: 0; top: 182px; justify-content: center; }
  .card-back .brand-dot { background: #ffffff; }
  .card-back .brand-name { color: #ffffff; font-size: 32px; }

  .holder { position: absolute; left: 42px; top: 232px; }
  .holder-name {
    font-family: "Montserrat", Arial, sans-serif;
    font-weight: 600; font-size: 23px; color: var(--ink);
  }
  .holder-title { font-size: 17px; color: var(--teal); margin-top: 0; }

  .divider { position: absolute; left: 42px; right: 44px; top: 294px; height: 1px; background: var(--rule); }

  .contacts { position: absolute; left: 42px; top: 311px; display: flex; font-size: 16px; color: var(--ink-soft); }
  .contact-col { padding-right: 15px; margin-right: 15px; border-right: 1px solid var(--teal); }
  .contact-col:last-child { border-right: none; margin-right: 0; padding-right: 0; }
  .contact-row { display: flex; align-items: center; height: 23px; white-space: nowrap; }
  .contact-row svg { width: 15px; height: 15px; margin-right: 13px; fill: var(--teal); flex: none; }

  .address-band {
    position: absolute; left: 0; right: 0; top: 380px; height: 32px;
    background: var(--teal); color: #ffffff; font-size: 16px;
    display: flex; align-items: center; justify-content: center;
  }
  .address-band svg { width: 13px; height: 15px; fill: #ffffff; margin-right: 8px; }

  .back-url {
    position: absolute; left: 0; right: 0; top: 374px;
    text-align: center; color: #ffffff; font-size: 15px; letter-spacing: 0.03em;
  }
</style>
</head>
<body>

<section class="card card-front">
  <svg class="ghost-ring" width="330" height="330" viewBox="0 0 330 330" aria-hidden="true">
    <circle cx="165" cy="165" r="140" fill="none" stroke="var(--ghost)" stroke-width="26"/>
  </svg>

  <div class="brand">
    <span class="brand-dot"></span>
    <div class="brand-name"><span>Brill Insurance</span><span class="sub">Agency Inc</span></div>
  </div>

  <div class="holder">
    <div class="holder-name">MARTIN VALE</div>
    <div class="holder-title">Insurance&nbsp; Agent</div>
  </div>

  <div class="divider"></div>

  <div class="contacts">
    <div class="contact-col">
      <div class="contact-row">
        <svg viewBox="0 0 24 24"><path d="M6.6 10.8a15.1 15.1 0 0 0 6.6 6.6l2.2-2.2c.3-.3.7-.4 1-.2 1.1.4 2.3.6 3.6.6.6 0 1 .4 1 1V20c0 .6-.4 1-1 1A17 17 0 0 1 3 4c0-.6.4-1 1-1h3.5c.6 0 1 .4 1 1 0 1.3.2 2.5.6 3.6.1.3 0 .7-.2 1z"/></svg>
        Business : 555-213-4087
      </div>
      <div class="contact-row">
        <svg viewBox="0 0 24 24"><path d="M6.6 10.8a15.1 15.1 0 0 0 6.6 6.6l2.2-2.2c.3-.3.7-.4 1-.2 1.1.4 2.3.6 3.6.6.6 0 1 .4 1 1V20c0 .6-.4 1-1 1A17 17 0 0 1 3 4c0-.6.4-1 1-1h3.5c.6 0 1 .4 1 1 0 1.3.2 2.5.6 3.6.1.3 0 .7-.2 1z"/></svg>
        Toll Free : 888-555-0194
      </div>
    </div>
    <div class="contact-col">
      <div class="contact-row">
        <svg viewBox="0 0 24 24"><path d="M6 3h12v4H6zM4 8h16a2 2 0 0 1 2 2v6h-4v5H6v-5H2v-6a2 2 0 0 1 2-2zm4 7v4h8v-4z"/></svg>
        555-213-7751
      </div>
      <div class="contact-row">
        <svg viewBox="0 0 24 24"><path d="M12 3 2 12h3v9h5v-6h4v6h5v-9h3z"/></svg>
        555-390-2618
      </div>
    </div>
    <div class="contact-col">
      <div class="contact-row">
        <svg viewBox="0 0 24 24"><path d="M2 5h20v14H2zm2 2v.5l8 5 8-5V7z"/></svg>
        mvale@brillagency.com
      </div>
      <div class="contact-row">
        <svg viewBox="0 0 24 24"><path d="M12 2a10 10 0 1 0 0 20 10 10 0 0 0 0-20zm6.9 6h-2.9a15 15 0 0 0-1.4-3.6A8 8 0 0 1 18.9 8zM12 4c.8 1.2 1.5 2.5 1.9 4h-3.8c.4-1.5 1.1-2.8 1.9-4zM4.3 14a8 8 0 0 1 0-4h3.4a16 16 0 0 0 0 4zm.8 2h2.9c.4 1.3.8 2.5 1.4 3.6A8 8 0 0 1 5.1 16zM8 8H5.1a8 8 0 0 1 4.3-3.6C8.8 5.5 8.4 6.7 8 8zm4 12c-.8-1.2-1.5-2.5-1.9-4h3.8c-.4 1.5-1.1 2.8-1.9 4zm2.3-6H9.7a14 14 0 0 1 0-4h4.6a14 14 0 0 1 0 4zm.3 5.6c.6-1.1 1-2.3 1.4-3.6h2.9a8 8 0 0 1-4.3 3.6zm1.7-5.6a16 16 0 0 0 0-4h3.4a8 8 0 0 1 0 4z"/></svg>
        www.brillagency.net
      </div>
    </div>
  </div>

  <div class="address-band">
    <svg viewBox="0 0 24 28"><path d="M12 0a10 10 0 0 0-10 10c0 7.5 10 18 10 18s10-10.5 10-18A10 10 0 0 0 12 0zm0 14a4 4 0 1 1 0-8 4 4 0 0 1 0 8z"/></svg>
    42 W Elm Rd, Butler, MO 64730
  </div>
</section>

<section class="card card-back">
  <div class="brand">
    <span class="brand-dot"></span>
    <div class="brand-name"><span>Brill Insurance</span><span class="sub">Agency Inc</span></div>
  </div>
  <div class="back-url">www.brillagency.net</div>
</section>

</body>
</html>
```